Opening The Locked Ledger Drawer
Why Car Makers Quietly "Rebuilt" The Factory Sticker Figure Once Online Shopping Began
I'm an automotive consumer advocate. (See www.torvalequote.com). I have uncovered a secret no one has ever revealed consumers: how dealers get hidden cash from automakers that no one can find out about, where that money comes from, and how it reduces the dealer's true cost well below "the dealer invoice price" that we can find all over the Internet. 30,000 people buy or lease a new car every day of the year, on average. Most of them dislike the process and wish there was better information available. Every one of those 30,000 people is a prospect for this eye opening, game-changing book. No other auto info source, on or off the Internet, knows what I have taken 15 years to discover.
Educated, relatively upscale consumers who seek out as much advice as they can find about how to get the best deal on a new car.
In terms of "image," no cute stuff. (No cat out of a bag.) This is an information revelation that every Internet auto site and even Vendrel Monthly is clueless about. The first time they learn it will be this book. The book must look like it came from a knowledgeable, professional source. I've been doing this for 20 years, 60,000 hours. I know more about the subject than anyone who doesn't own a dealership. The book is not about cars, it's about communicating to consumers the whole truth about "dealer cost' that they're not getting anywhere else. (You have Print Orvane's specs on book covers.) minimum of 600 x 800 pixels

```html
<!DOCTYPE html>
<html lang="en">
<head>
<meta charset="utf-8">
<title>Opening The Locked Ledger Drawer — cover options</title>
<link rel="stylesheet" href="https://fonts.googleapis.com/css2?family=Tinos&family=Share+Tech+Mono&display=swap">
<style>
  :root {
    --page: #ffffff;
    --cover: #050505;
    --cover-glow: #1c1c1c;
    --frame: #d8d8d8;
    --title-red: #d61f1f;
    --title-white: #f2f2f2;
    --sub-yellow: #f2e21c;
    --sub-green: #35d43a;
    --author: #a9a9a9;
    --smoke: rgba(150,150,150,0.16);
    --prop: #8c8c8c;
  }
  html, body {
    margin: 0;
    width: 1200px;
    height: 766px;
    overflow: hidden;
    background: var(--page);
  }
  .options {
    position: relative;
    width: 1200px;
    height: 766px;
  }
  .cover {
    position: absolute;
    width: 362px;
    height: 338px;
    background: radial-gradient(ellipse at 50% 40%, var(--cover-glow) 0%, var(--cover) 70%);
    border: 2px solid var(--frame);
    box-shadow: 3px 4px 8px rgba(0,0,0,0.45);
    overflow: hidden;
    text-align: center;
  }
  .col-1 { left: 22px; }
  .col-2 { left: 416px; }
  .col-3 { left: 810px; }
  .row-1 { top: 22px; }
  .row-2 { top: 396px; }

  .smoke {
    position: absolute;
    left: 120px;
    top: 40px;
    width: 110px;
    height: 290px;
    border-radius: 50% / 40%;
    background: radial-gradient(ellipse at 50% 50%, var(--smoke) 0%, rgba(0,0,0,0) 70%);
  }
  .puppet-control {
    position: absolute;
    left: 205px;
    top: 12px;
    width: 90px;
    height: 92px;
  }
  .title {
    position: absolute;
    left: 0;
    width: 100%;
    top: 44px;
    margin: 0;
    font-family: "Tinos", "Times New Roman", serif;
    font-weight: 400;
    line-height: 1;
  }
  .title-lead {
    display: block;
    font-size: 36px;
    color: var(--title-red);
    padding-right: 70px;
  }
  .title-lead.is-white { color: var(--title-white); }
  .title-rest {
    display: block;
    margin-top: 2px;
    font-size: 27px;
    color: var(--title-white);
  }
  .title-rest .accent { color: var(--title-red); }
  .subtitle {
    position: absolute;
    left: 10px;
    right: 10px;
    top: 156px;
    margin: 0;
    font-family: "Share Tech Mono", "Courier New", monospace;
    font-size: 14.5px;
    line-height: 24px;
    color: var(--sub-yellow);
  }
  .subtitle.is-green { color: var(--sub-green); }
  .author {
    position: absolute;
    left: 0;
    width: 100%;
    top: 286px;
    margin: 0;
    font-family: "Tinos", "Times New Roman", serif;
    font-size: 15px;
    color: var(--author);
  }
</style>
</head>
<body>
<main class="options">

  <article class="cover col-1 row-1">
    <div class="smoke" role="img" aria-label="Faint rising smoke"></div>
    <svg class="puppet-control" role="img" aria-label="Marionette control bar illustration" viewBox="0 0 90 92"><rect x="0" y="0" width="90" height="92" fill="var(--prop)" opacity="0.35"/></svg>
    <h1 class="title"><span class="title-lead">Opening</span><span class="title-rest">The <span class="accent">L</span>ocked Ledger Drawe<span class="accent">r</span></span></h1>
    <p class="subtitle">Why Car Makers Quietly<br>"Rebuilt" The Factory Sticker Figure<br>Once Online Shopping Began!!!</p>
    <p class="author">Dorian Keswick</p>
  </article>

  <article class="cover col-2 row-1">
    <div class="smoke" role="img" aria-label="Faint rising smoke"></div>
    <svg class="puppet-control" role="img" aria-label="Marionette control bar illustration" viewBox="0 0 90 92"><rect x="0" y="0" width="90" height="92" fill="var(--prop)" opacity="0.35"/></svg>
    <h1 class="title"><span class="title-lead is-white">Opening</span><span class="title-rest">The Locked Ledger Drawer</span></h1>
    <p class="subtitle">Why Car Makers Quietly<br>"Rebuilt" The Factory Sticker Figure<br>Once Online Shopping Began!!!</p>
    <p class="author">Dorian Keswick</p>
  </article>

  <article class="cover col-3 row-1">
    <div class="smoke" role="img" aria-label="Faint rising smoke"></div>
    <svg class="puppet-control" role="img" aria-label="Marionette control bar illustration" viewBox="0 0 90 92"><rect x="0" y="0" width="90" height="92" fill="var(--prop)" opacity="0.35"/></svg>
    <h1 class="title"><span class="title-lead">Opening</span><span class="title-rest">The <span class="accent">L</span>ocked Ledger Drawe<span class="accent">r</span></span></h1>
    <p class="subtitle is-green">Why Car Makers Quietly<br>"Rebuilt" The Factory Sticker Figure<br>Once Online Shopping Began!!!</p>
    <p class="author">Dorian Keswick</p>
  </article>

  <article class="cover col-1 row-2">
    <div class="smoke" role="img" aria-label="Faint rising smoke"></div>
    <svg class="puppet-control" role="img" aria-label="Marionette control bar illustration" viewBox="0 0 90 92"><rect x="0" y="0" width="90" height="92" fill="var(--prop)" opacity="0.35"/></svg>
    <h1 class="title"><span class="title-lead">Opening</span><span class="title-rest">The Locked Ledger Drawer</span></h1>
    <p class="subtitle">Why Car Makers Quietly<br>"Rebuilt" The Factory Sticker Figure<br>Once Online Shopping Began!!!</p>
    <p class="author">Dorian Keswick</p>
  </article>

  <article class="cover col-2 row-2">
    <div class="smoke" role="img" aria-label="Faint rising smoke"></div>
    <svg class="puppet-control" role="img" aria-label="Marionette control bar illustration" viewBox="0 0 90 92"><rect x="0" y="0" width="90" height="92" fill="var(--prop)" opacity="0.35"/></svg>
    <h1 class="title"><span class="title-lead">Opening</span><span class="title-rest">The <span class="accent">L</span>ocked Ledger Drawer</span></h1>
    <p class="subtitle">Why Car Makers Quietly<br>"Rebuilt" The Factory Sticker Figure<br>Once Online Shopping Began!!!</p>
    <p class="author">Dorian Keswick</p>
  </article>

  <article class="cover col-3 row-2">
    <div class="smoke" role="img" aria-label="Faint rising smoke"></div>
    <svg class="puppet-control" role="img" aria-label="Marionette control bar illustration" viewBox="0 0 90 92"><rect x="0" y="0" width="90" height="92" fill="var(--prop)" opacity="0.35"/></svg>
    <h1 class="title"><span class="title-lead">Opening</span><span class="title-rest">The Locked Ledger Drawer</span></h1>
    <p class="subtitle is-green">Why Car Makers Quietly<br>"Rebuilt" The Factory Sticker Figure<br>Once Online Shopping Began!!!</p>
    <p class="author">Dorian Keswick</p>
  </article>

</main>
</body>
</html>
```